目的:転職を検討している看護師さんの集客
対象:20~39歳の女性看護師
利用:SEMやバナーからリンクさせます。ゴールは登録ボタンです。
幅770px程度、高さ指定なし
http://www.kenkou-staffnet.com/
若い女性向けの色使い(可愛い、ステキ、優しい、親しみが持てる、安心というイメージ)
地域、電話番号の欄は編集可能な状態でお願いいたします。
デザインに必要な原稿や素材はご用意いたします。
キャラクター素材については、表情やポーズなど作り直しできますので仰ってください。
別途お持ちの素材等がありましたらご使用いただき、良い素材があれば有料のものでもご提案ください(高すぎないものでしたら助かります)
コーディングや写真の切り出し、簡単な文章の修正はこちらで可能です。

以下のサイトはイメージに近いです。
http://hoken.538.co.jp/lp/entry/k4312/00/tokyo/
http://www.carestarjp.jp/nmtlp_1101-1/
http://www.byouinnomirai.jp/lp/lp_7.html
http://www.byouinnomirai.jp/lp/lp_11.html

(看護師さんに魅力を感じていただければ、まったく別のイメージでも構いません)

デザインをしていただく上でご提案などあれば、ご遠慮なく仰ってください。
(土日祝日のお返事は、休み明けとなりますのでご了承ください)

今後も複数のLPを制作予定ですので、今回良いランディングページを作成いただいた方と引き続き、お付き合いさせていただければと思っております。
それでは、ご提案をお待ちしております。よろしくお願いいたします。
ご覧いただきましてありがとうございます。
弊社にて、以下の画像を購入しております。
制作にあたり必要がございましたら、お申し付けください。
http://gazoubako.net/search_title/title_detail.aspx?id=3027

(利用範囲は購入元の著作権に準じます)

皆さんから多くのご提案をいただけて、とても感謝しております。
どの作品も素晴らしく社内で二度三度と協議し、最後まで悩みに悩んで決めさせていただきました。
デザイン・構成はもちろん、競合他社にないイメージを作っていただいたことが決め手になりました。
若い女性がターゲットということもあり、最後は同年代女性スタッフによる多数決でこちらのご提案を採用させていただきました。

mintopupu様のやわらかく親しみやすいデザイン、rtsv様のファーストビューから受ける信頼感、MELBRIXA様の「ひとりで転職」欄の負担が感じられる表現、*ru-mi*様のしっかりした出元を感じさせる色づかい、PLATINESCOVE様のファーストビューから受ける好印象、TWM42様の手書き文字&イラストのクオリティの高さ、bruno456様の斬新なご提案など、ひとつひとつの工夫や力量に深い感銘を受けました。
今後もバナーやLP中心に作成を予定していて、こちらを利用させて頂く機会も多々あると思いますので、またご参加いただけると嬉しいです。

```html
<!DOCTYPE html>
<html lang="ja">
<head>
<meta charset="UTF-8">
<title>あなただけの転職サポート</title>
<link rel="stylesheet" href="https://fonts.googleapis.com/css2?family=M+PLUS+Rounded+1c:wght@400;700;800;900&family=Noto+Sans+JP:wght@400;700;900&display=swap">
<style>
:root{
  --pink:#e8477a;
  --pink-deep:#c93563;
  --pink-soft:#f8d3dc;
  --pink-pale:#fdeef2;
  --pink-board:#f3aebd;
  --rose:#b84458;
  --orange:#f39a2b;
  --orange-deep:#e0761a;
  --teal:#3bb3b0;
  --green:#5cb531;
  --navy:#2d4f8a;
  --ink:#3b3335;
  --white:#ffffff;
}
*{margin:0;padding:0;box-sizing:border-box}
html,body{width:1200px;height:3336px;overflow:hidden}
body{
  position:relative;
  font-family:"M PLUS Rounded 1c","Noto Sans JP",sans-serif;
  color:var(--ink);
  background:
    repeating-linear-gradient(90deg,rgba(255,255,255,.35) 0 6px,transparent 6px 22px),
    var(--pink-soft);
}
.abs{position:absolute}
.fill{position:absolute;border-radius:8px}
.nowrap{white-space:nowrap}

/* header */
.hero{position:absolute;left:0;top:0;width:1200px;height:760px;
  background:linear-gradient(180deg,#fbe3e9 0%,#f7c9d4 70%,#f4bccb 100%)}
.hero-photo{left:780px;top:0;width:420px;height:520px;border-radius:0 0 0 200px;
  background:radial-gradient(circle at 55% 35%,#fff 0%,#f6e4df 45%,#f2c8d2 100%)}
.badge-local{left:60px;top:20px;width:400px;height:205px;text-align:center;
  background:linear-gradient(180deg,#fff 0%,#fde7ed 100%);border:4px solid #f2a7b9;border-radius:24px;padding-top:16px}
.badge-local .l1{font-size:36px;font-weight:800;color:var(--rose);letter-spacing:4px}
.badge-local .l2{font-size:32px;font-weight:700;color:var(--rose)}
.badge-local .l3{font-size:62px;font-weight:900;color:var(--pink);line-height:1.1;display:flex;justify-content:center;align-items:center;gap:10px}
.top-claim{left:540px;top:34px;font-size:48px;font-weight:900;color:var(--pink-deep);display:flex;align-items:center;gap:6px;white-space:nowrap}
.top-claim .area{display:inline-flex;width:56px;height:56px;border-radius:50%;background:var(--pink-deep);color:#fff;
  font-size:36px;align-items:center;justify-content:center}
.pro-tag{left:480px;top:150px;height:54px;padding:0 24px;background:var(--pink);color:#fff;font-size:34px;font-weight:800;
  line-height:54px;border-radius:8px;white-space:nowrap}
.catch-1{left:60px;top:210px;font-size:112px;line-height:1.15;font-weight:900;color:var(--ink);letter-spacing:2px;white-space:nowrap}
.catch-2{left:50px;top:340px;font-size:128px;line-height:1.15;font-weight:900;color:var(--pink);letter-spacing:4px;white-space:nowrap;
  text-shadow:0 6px 0 #fff}
.merit{width:210px;height:210px;border-radius:50%;background:radial-gradient(circle at 40% 35%,#fff 0%,#fde3ea 60%,#f6b7c7 100%);
  border:5px solid #fff;box-shadow:0 4px 0 #e7a0b3;text-align:center;color:var(--pink-deep)}
.merit .k{display:inline-block;margin-top:28px;background:var(--pink);color:#fff;font-size:20px;font-weight:700;padding:2px 14px;border-radius:16px}
.merit .v{font-size:58px;font-weight:900;line-height:1.05;margin-top:6px;white-space:nowrap}
.merit .v small{font-size:26px}
.merit .s{font-size:20px;font-weight:700;color:var(--rose)}
.cta-top{left:580px;top:520px;width:540px;height:100px;border-radius:18px;
  background:linear-gradient(180deg,#fff 0%,#f1f5fb 100%);border:4px solid #9fb5d6;display:flex;align-items:center;padding:0 14px;gap:12px}
.free{background:var(--green);color:#fff;font-weight:900;font-size:36px;padding:4px 12px;border-radius:8px;white-space:nowrap}
.cta-top .t{font-size:28px;font-weight:800;color:var(--navy);flex:1;white-space:nowrap}
.arrow-dot{width:56px;height:56px;border-radius:50%;background:var(--navy);display:flex;align-items:center;justify-content:center;flex:none}
.phone{left:600px;top:645px;display:flex;align-items:center;gap:14px;font-size:56px;font-weight:900;color:var(--navy);font-family:"Noto Sans JP",sans-serif;white-space:nowrap}

/* trial ribbon + comparison */
.ribbon{left:220px;top:820px;width:760px;height:70px;background:var(--rose);color:#fff;text-align:center;white-space:nowrap;
  font-size:40px;font-weight:900;line-height:70px;border-radius:10px;box-shadow:0 6px 0 #8f2f40;z-index:2}
.compare{left:140px;top:910px;width:920px;height:640px;background:#fff8f0;border:6px solid #f4c28f;border-radius:14px}
.tab{top:940px;height:66px;line-height:66px;text-align:center;font-size:32px;font-weight:800;border-radius:8px;white-space:nowrap}
.tab.alone{left:165px;width:300px;background:#d9d6d7;color:#555}
.tab.pro{left:500px;width:540px;background:var(--orange);color:#fff}
.alone-illust{left:165px;top:1025px;width:300px;height:250px;background:linear-gradient(180deg,#f3f1f2,#dcd8da)}
.alone-photo{left:175px;top:1285px;width:290px;height:245px;background:linear-gradient(180deg,#efe2dc,#cdb8b4)}
.to-pro{left:462px;top:1170px}
.pro-illust{left:505px;top:1025px;width:250px;height:260px;background:linear-gradient(180deg,#fff3e4,#fbd9c3)}
.memo{left:518px;top:1042px;width:225px;height:140px;background:#fff;border:2px solid #e6c3a0;border-radius:6px;padding:10px 12px;
  font-size:21px;line-height:1.7;color:#6a5a4d;white-space:nowrap}
.pro-list{left:770px;top:1030px;width:270px}
.pro-list li{list-style:none;display:flex;align-items:center;gap:10px;height:74px;margin-bottom:8px;background:#fff;border:3px solid #f7c9a0;border-radius:10px;padding:0 10px;font-size:24px;font-weight:700;color:var(--orange-deep);line-height:1.2}
.pro-list .ico{width:44px;height:44px;border-radius:50%;background:#fbe0c8;flex:none}
.bubble-happy{left:560px;top:1315px;width:460px;height:150px;background:#fff;border:4px solid #f39a2b;border-radius:70px;
  text-align:center;padding-top:22px;font-size:28px;font-weight:800;color:var(--ink);line-height:1.4;white-space:nowrap}

/* nurse talk section */
.talk{left:140px;top:1570px;width:920px;height:590px;background:linear-gradient(160deg,#fde7ed 0%,#f7c2cf 100%);border-radius:14px}
.doctor-photo{left:160px;top:1600px;width:320px;height:320px;background:linear-gradient(180deg,#f4f6f8,#cfd9e2)}
.woman-photo{left:600px;top:1650px;width:330px;height:500px;background:linear-gradient(180deg,#f5e6e0,#d9b9b8)}
.bubble-ask{left:380px;top:1585px;width:340px;height:110px;background:#eeeeee;border-radius:40px;padding:16px 24px;z-index:3;
  font-size:28px;font-weight:800;line-height:1.4;color:var(--ink);white-space:nowrap}
.heart{left:910px;top:1680px;width:150px;height:140px;z-index:3}
.heart span{position:absolute;left:0;top:42px;width:150px;text-align:center;color:#fff;font-size:26px;font-weight:900;white-space:nowrap}
.teal-banner{left:330px;top:1935px;width:560px;height:160px;border-radius:80px;background:var(--teal);border:6px solid #fff;z-index:3;
  color:#fff;text-align:center;font-size:38px;font-weight:900;line-height:1.4;padding-top:24px;box-shadow:0 6px 0 #2a8a88;white-space:nowrap}

/* promises */
.promise-head{left:250px;top:2185px;width:700px;height:64px;background:var(--orange);color:#fff;text-align:center;
  font-size:42px;font-weight:900;line-height:64px;border-radius:32px;white-space:nowrap}
.board{left:140px;top:2265px;width:920px;height:500px;background:var(--pink-board);border-radius:14px}
.card{top:2290px;width:270px;height:450px;background:#fffdf6;border:3px solid #e9c9a8;border-radius:8px;padding:22px 16px;text-align:center}
.card .pre{font-size:18px;font-weight:700;color:var(--pink);white-space:nowrap}
.card h3{display:flex;align-items:center;justify-content:center;gap:8px;font-size:34px;font-weight:900;color:var(--pink-deep);white-space:nowrap;
  margin:12px 0 18px;border-bottom:3px dotted #f2a7b9;padding-bottom:14px}
.card h3 .n{width:46px;height:46px;border-radius:8px;background:var(--pink-deep);color:#fff;font-size:32px;line-height:46px;flex:none}
.card p{font-size:24px;line-height:1.6;font-weight:700;text-align:left;color:#5a4a4d}
.card p b{color:var(--pink-deep)}

/* call to action */
.ask-arrow{left:220px;top:2780px}
.ok-dot{left:545px;top:2915px;width:110px;height:110px;border-radius:50%;background:#fff;border:4px solid var(--pink);
  color:var(--pink);font-size:20px;font-weight:900;text-align:center;line-height:1.2;display:flex;align-items:center;justify-content:center;z-index:2}
.cta-main{left:220px;top:3040px;width:760px;height:130px;border-radius:24px;background:linear-gradient(180deg,#fff 0%,#eef3fa 100%);
  border:6px solid #9fb5d6;display:flex;align-items:center;padding:0 20px;gap:18px;box-shadow:0 8px 0 #7f97bd}
.cta-main .free{font-size:44px;padding:6px 16px}
.cta-main .t{font-size:40px;font-weight:900;color:var(--navy);flex:1;white-space:nowrap}
.cta-main .arrow-dot{width:76px;height:76px}
.click{left:70px;top:3060px;font-size:40px;font-weight:900;color:var(--pink);line-height:1.2}
.chara-bubble{left:990px;top:2960px;width:180px;height:80px;background:#fff;border-radius:20px;font-size:17px;font-weight:700;
  line-height:1.4;padding:12px;color:var(--ink);white-space:nowrap}
.chara{left:1010px;top:3060px;width:150px;height:120px;border-radius:60px;background:linear-gradient(180deg,#fde3ea,#f5b3c4)}
.license{left:490px;top:3220px;width:220px;height:44px;background:#fff;border:2px solid #e7a9b8;text-align:center;font-size:22px;
  font-weight:700;line-height:40px;color:var(--rose);white-space:nowrap}
</style>
</head>
<body>

<section class="hero">
  <div class="fill hero-photo abs" role="img" aria-label="白衣姿で微笑む看護師の写真"></div>

  <div class="badge-local abs">
    <div class="l1">地域密着</div>
    <div class="l2">看護師さんに選ばれて</div>
    <div class="l3">
      <svg width="60" height="48" viewBox="0 0 60 48" aria-hidden="true"><path d="M4 42 L8 10 L20 26 L30 4 L40 26 L52 10 L56 42 Z" fill="#f3b43a" stroke="#c98a16" stroke-width="3"/></svg>
      NO.1
    </div>
  </div>

  <div class="top-claim abs"><span class="area">地</span><span class="area">域</span><span class="area">名</span>の求人数NO.1</div>

  <div class="pro-tag abs">健康スタッフのプロが</div>
  <div class="catch-1 abs">あなただけの</div>
  <div class="catch-2 abs">転職サポート</div>

  <div class="merit abs" style="left:90px;top:520px">
    <span class="k">年収例</span>
    <div class="v">600<small>万円</small></div>
    <div class="s">平均420万円</div>
  </div>
  <div class="merit abs" style="left:330px;top:520px">
    <span class="k">休日</span>
    <div class="v">130<small>日</small></div>
    <div class="s">平均90日</div>
  </div>

  <div class="cta-top abs">
    <span class="free">無料</span>
    <span class="t">転職サポートを申し込む</span>
    <span class="arrow-dot"><svg width="24" height="24" viewBox="0 0 24 24"><path d="M8 4 L18 12 L8 20 Z" fill="#fff"/></svg></span>
  </div>
  <div class="phone abs">
    <svg width="60" height="50" viewBox="0 0 50 50" aria-hidden="true"><circle cx="25" cy="25" r="22" fill="none" stroke="#2d4f8a" stroke-width="5"/><path d="M16 15 q-3 10 8 21 q6 5 10 3 l3-4 l-6-5 l-3 3 q-6-3-8-10 l3-2 l-4-7 z" fill="#2d4f8a"/></svg>
    0120.000.000
  </div>
</section>

<div class="ribbon abs">ためしてみて！らくらくサポート！</div>

<section class="compare abs" aria-label="ひとりで転職とプロにおまかせの比較"></section>
<div class="tab alone abs">一人で転職の場合</div>
<div class="tab pro abs">あなただけのプロにおまかせ</div>
<div class="fill alone-illust abs" role="img" aria-label="求人を一人で探し疲れる様子のイラスト"></div>
<div class="fill alone-photo abs" role="img" aria-label="頭を抱えて悩む女性の写真"></div>
<svg class="to-pro abs" width="46" height="80" viewBox="0 0 46 80" aria-hidden="true"><path d="M4 20 H24 V4 L44 40 L24 76 V60 H4 Z" fill="#f39a2b"/></svg>
<div class="fill pro-illust abs" role="img" aria-label="相談にのる担当コンサルタントのイラスト"></div>
<div class="memo abs">□お休み取りたい<br>□年収UP<br>□残業少ない</div>
<ul class="pro-list abs">
  <li><span class="ico"></span>非公開の募集</li>
  <li><span class="ico"></span>保育所ありの<br>好条件</li>
  <li><span class="ico"></span>内緒の裏話</li>
</ul>
<div class="bubble-happy abs">わがままいったのに<br>アピールも電話も交渉も<br>ぜーんぶやってもらっちゃった！</div>

<section class="talk abs"></section>
<div class="fill doctor-photo abs" role="img" aria-label="聴診器を持つ女性看護師の写真"></div>
<div class="fill woman-photo abs" role="img" aria-label="スーツ姿で微笑む女性コンサルタントの写真"></div>
<div class="bubble-ask abs">行きたい○○病院の<br>募集が出たら教えて！</div>
<div class="heart abs">
  <svg width="150" height="140" viewBox="0 0 150 140" aria-hidden="true"><path d="M75 132 C10 86 0 54 14 28 C30 2 64 6 75 32 C86 6 120 2 136 28 C150 54 140 86 75 132 Z" fill="#ee6b93"/></svg>
  <span>ありがと！</span>
</div>
<div class="teal-banner abs">人間関係ホントのとこ<br>残業時間・離職率教えます！</div>

<div class="promise-head abs">あなたと約束します。</div>
<section class="board abs"></section>
<article class="card abs" style="left:165px">
  <div class="pre">あなたのワガママ</div>
  <h3><span class="n">1</span>特別採用枠</h3>
  <p>全国○万件の掲載病院からの求人依頼は<b>健康スタッフ</b>だけ！</p>
</article>
<article class="card abs" style="left:465px">
  <div class="pre">あなたのプライバシー守る</div>
  <h3><span class="n">2</span>応募前診断</h3>
  <p>匿名で給料も条件もわかります！面接も「面接後のお断り」もすべて代わりにします！</p>
</article>
<article class="card abs" style="left:765px">
  <div class="pre">あなたの悩み解決</div>
  <h3><span class="n">3</span>円満退職</h3>
  <p>やめずらくて…の悩みもスッキリ！<b>退職まで</b>しっかりサポートします！</p>
</article>

<svg class="ask-arrow abs" width="760" height="190" viewBox="0 0 760 190" aria-hidden="true">
  <path d="M40 0 H720 V90 H760 L380 190 L0 90 H40 Z" fill="#f39a2b"/>
  <text x="380" y="80" text-anchor="middle" font-family="'M PLUS Rounded 1c',sans-serif" font-size="62" font-weight="900" fill="#fff">とりあえず聞いてみる</text>
</svg>
<div class="ok-dot abs">だけでも<br>OK！</div>

<div class="click abs">click<br>here!</div>
<div class="cta-main abs">
  <span class="free">無料</span>
  <span class="t">転職サポートを申し込む</span>
  <span class="arrow-dot"><svg width="32" height="32" viewBox="0 0 24 24"><path d="M8 4 L18 12 L8 20 Z" fill="#fff"/></svg></span>
</div>
<div class="chara-bubble abs">今なら転職の悩み<br>なんでも相談OK</div>
<div class="chara abs" role="img" aria-label="ピンクのマスコットキャラクター"></div>

<div class="license abs">厚生労働省認可</div>

</body>
</html>
```